i need a Star Circuit blog design

hi, i need a blog which have Star Circuit news. My blog should be attractive and mature with a good theme. Readers of my blog should be able to comment. You can include any attractive colour (blue, green, purple, red).

Target Market(s)

Celebrity fans and enthusiasts

Industry/Entity Type

News

```html
<!DOCTYPE html>
<html lang="en">
<head>
<meta charset="utf-8">
<title>Star Circuit</title>
<link rel="stylesheet" href="https://fonts.googleapis.com/css2?family=Arimo:wght@700&family=Open+Sans:ital,wght@0,400;0,600;1,400&display=swap">
<style>
:root{
  --purple:#52077f;
  --purple-dark:#3f0565;
  --nav:#414141;
  --nav-active:#2d2d2d;
  --page:#f0eeec;
  --card:#ffffff;
  --panel:#f4f4f4;
  --line:#d9d9d9;
  --red:#d0101f;
  --blue-link:#1d6fa5;
  --text:#3a3a3a;
  --icon:#1c5f97;
  --fb:#2d4a8c;
  --tw1:#5bcaf6;
  --tw2:#2eb4ef;
  --pin:#c20a1f;
  --footer:#29292c;
}
*{box-sizing:border-box;margin:0;padding:0}
html,body{width:922px;height:1200px;overflow:hidden}
body{position:relative;background:var(--page);font-family:"Open Sans",sans-serif;color:var(--text)}
.abs{position:absolute}
.masthead{left:0;top:0;width:922px;height:92px;background:linear-gradient(var(--purple),var(--purple-dark))}
.brand{left:77px;top:28px;font-family:"Arimo",sans-serif;font-weight:700;font-size:22px;color:#fff;letter-spacing:.3px}
.search{left:680px;top:31px;width:166px;height:22px;background:#fff;border-radius:3px;border:1px solid #ccc;overflow:hidden}
.search-btn{position:absolute;right:0;top:0;width:24px;height:20px;background:var(--purple);border-left:1px solid #ddd}
.mainnav{left:0;top:92px;width:922px;height:45px;background:var(--nav)}
.mainnav a{position:absolute;top:0;height:45px;line-height:45px;color:#fff;font-size:10px;text-decoration:none;transform:translateX(-50%);letter-spacing:.2px}
.mainnav .active{left:77px;width:72px;transform:none;text-align:center;background:var(--nav-active)}
.hero{left:0;top:137px;width:922px;height:302px;background:linear-gradient(100deg,#c9b7a1 0%,#8c9a5c 45%,#6f8f3c 70%,#5d8a34 100%)}
.dots{left:435px;top:408px;display:flex;gap:5px}
.dots span{width:9px;height:9px;border-radius:50%;background:#777;border:1px solid #eee}
.dots span.on{background:var(--purple)}
.card{background:var(--card);border:1px solid #dcdcdc;box-shadow:0 0 3px rgba(0,0,0,.08)}
.main{left:77px;top:455px;width:500px;height:580px}
.section-title{color:var(--red);font-size:13px;font-weight:600}
.post{left:18px;width:457px;background:var(--panel);border:1px solid #e0e0e0}
.post h2{position:absolute;left:14px;top:10px;font-size:11.5px;font-weight:400;color:var(--blue-link)}
.post p{position:absolute;left:15px;top:30px;width:300px;font-size:7.5px;line-height:13px;color:#444}
.post .photo{position:absolute;left:15px;top:63px;width:428px;height:131px}
.post-meta{position:absolute;left:-1px;bottom:-1px;width:457px;height:37px;background:#fff;border:1px solid #ccc;display:flex;align-items:center;padding-left:16px;gap:13px;font-size:7.5px;font-style:italic;color:#333}
.post-meta span{display:flex;align-items:center;gap:5px}
.pager{left:241px;top:550px;display:flex;align-items:center;gap:6px;font-size:7.5px;color:#555}
.pager .cur{background:#333;color:#fff;width:16px;height:16px;line-height:16px;text-align:center;border-radius:2px}
.pager .last{color:var(--blue-link)}
.side{left:628px;top:455px;width:217px;height:580px}
.gossip-frame{left:8px;top:27px;width:200px;height:154px;border:1px solid #cfcfcf;background:#fff;padding:4px;box-shadow:0 0 2px rgba(0,0,0,.15)}
.gossip-frame div{width:100%;height:100%;background:linear-gradient(135deg,#9fb66a,#cfc2b0 55%,#6f9a3a)}
.widget{left:8px;width:199px;background:var(--panel);border:1px solid #ddd;box-shadow:0 1px 2px rgba(0,0,0,.12)}
.widget-head{height:26px;background:linear-gradient(var(--purple),var(--purple-dark));color:#fff;font-size:12px;line-height:26px;padding-left:10px}
.news-item{position:absolute;left:10px;width:178px;height:48px;border-bottom:1px solid var(--line)}
.news-item .thumb{position:absolute;left:0;top:3px;width:39px;height:32px}
.news-item p{position:absolute;left:47px;top:3px;font-size:7.5px;line-height:13px;color:#333}
.news-item.last{border-bottom:0}
.interview{position:absolute;left:11px;width:176px;height:25px;border-bottom:1px solid var(--line);font-size:7.5px;line-height:24px;color:#333}
.submit{position:absolute;left:12px;top:160px;font-size:10.5px;font-weight:600;color:var(--blue-link)}
.social-btn{top:1067px;height:33px;color:#fff;font-size:11.5px;font-weight:600;display:flex;align-items:center;justify-content:center;gap:10px;letter-spacing:.3px}
.social-btn .mark{width:13px;height:13px;border-radius:50%;background:#fff}
.fb{left:133px;width:208px;background:var(--fb);font-weight:400}
.fb .count{display:flex;align-items:center;gap:3px}
.fb .count i{display:block;width:30px;height:12px;background:#eef0f5;border-radius:2px}
.fb .count b{font-size:7px;color:#333;background:#fff;padding:1px 3px;border-radius:2px;font-weight:400}
.tw{left:357px;width:204px;background:linear-gradient(var(--tw1),var(--tw2))}
.pn{left:579px;width:211px;background:var(--pin)}
.footer{left:0;top:1122px;width:922px;height:78px;background:var(--footer)}
.footer-icons{left:386px;top:17px;display:flex;gap:3px}
.footer-icons span{width:18px;height:19px}
.copyright{left:0;top:51px;width:922px;text-align:center;font-size:7.5px;color:#888}
.copyright b{color:#ddd;font-weight:400}
</style>
</head>
<body>
<header class="abs masthead">
  <div class="abs brand">STAR CIRCUIT</div>
  <div class="abs search"><div class="search-btn">
    <svg width="24" height="20" viewBox="0 0 24 20"><circle cx="13" cy="9" r="3.2" fill="none" stroke="#fff" stroke-width="1.3"/><line x1="10.7" y1="11.3" x2="8" y2="14" stroke="#fff" stroke-width="1.5"/></svg>
  </div></div>
</header>

<nav class="abs mainnav">
  <a class="active" href="#">HOME</a>
  <a href="#" style="left:278px">ABOUT US</a>
  <a href="#" style="left:454px">LOCATION</a>
  <a href="#" style="left:620px">BLOG</a>
  <a href="#" style="left:793px">CONTACT US</a>
</nav>

<section class="abs hero" role="img" aria-label="Slideshow photo of a smiling couple sharing wine outdoors"></section>
<div class="abs dots"><span class="on"></span><span></span><span></span><span></span></div>

<main class="abs card main">
  <h1 class="abs section-title" style="left:18px;top:16px">BLOG ARTICLES</h1>

  <article class="abs post" style="top:34px;height:245px">
    <h2>Sed ut perspiciatis unde omnis &nbsp;sit voluptatem..</h2>
    <p>At vero eos et accusamus et iusto odio dignissimos ducimus qui blanditiis praesentium voluptatum deleniti atque</p>
    <div class="photo" role="img" aria-label="Photo of two women celebrating with champagne" style="background:linear-gradient(90deg,#2a2422,#5a4038 40%,#2b2524 70%,#3a3030)"></div>
    <div class="post-meta">
      <span><svg width="11" height="10" viewBox="0 0 11 10"><path d="M0 0h11v7H4L1.5 9.5V7H0z" fill="var(--icon)"/></svg>230</span>
      <span><svg width="8" height="8"><rect width="8" height="8" fill="var(--icon)"/></svg>230 Likes</span>
      <span><svg width="10" height="10"><circle cx="5" cy="5" r="5" fill="var(--icon)"/></svg>23 Shares</span>
      <span><svg width="10" height="10"><circle cx="5" cy="5" r="5" fill="var(--icon)"/></svg>23</span>
      <span><svg width="13" height="9" viewBox="0 0 13 9"><rect width="13" height="9" fill="var(--icon)"/><path d="M0 0l6.5 5L13 0" fill="none" stroke="#fff" stroke-width="1"/></svg>Email</span>
    </div>
  </article>

  <article class="abs post" style="top:293px;height:243px">
    <h2>Sed ut perspiciatis unde omnis &nbsp;sit voluptatem..</h2>
    <p>At vero eos et accusamus et iusto odio dignissimos ducimus qui blanditiis praesentium voluptatum deleniti atque</p>
    <div class="photo" role="img" aria-label="Photo of a woman in a sun hat and sunglasses" style="background:linear-gradient(90deg,#8a5a3a,#c79a6e 45%,#d9ae7c 55%,#7d5236)"></div>
    <div class="post-meta">
      <span><svg width="11" height="10" viewBox="0 0 11 10"><path d="M0 0h11v7H4L1.5 9.5V7H0z" fill="var(--icon)"/></svg>230</span>
      <span><svg width="8" height="8"><rect width="8" height="8" fill="var(--icon)"/></svg>230 Likes</span>
      <span><svg width="10" height="10"><circle cx="5" cy="5" r="5" fill="var(--icon)"/></svg>23 Shares</span>
      <span><svg width="10" height="10"><circle cx="5" cy="5" r="5" fill="var(--icon)"/></svg>23</span>
      <span><svg width="13" height="9" viewBox="0 0 13 9"><rect width="13" height="9" fill="var(--icon)"/><path d="M0 0l6.5 5L13 0" fill="none" stroke="#fff" stroke-width="1"/></svg>Email</span>
    </div>
  </article>

  <div class="abs pager"><span class="cur">1</span><span>&nbsp;2 &nbsp;|&nbsp; 3 &nbsp;|&nbsp; 4 &nbsp;|&nbsp; 5 &nbsp;|.....&nbsp; |</span><span class="last">LAST</span></div>
</main>

<aside class="abs card side">
  <h3 class="abs section-title" style="left:8px;top:6px;font-size:11.5px">GOSSIPS</h3>
  <div class="abs gossip-frame"><div role="img" aria-label="Photo of a man lying on the grass"></div></div>

  <section class="abs widget" style="top:192px;height:180px">
    <div class="widget-head">NEWS</div>
    <div class="news-item" style="top:36px"><div class="thumb" role="img" aria-label="News thumbnail" style="background:linear-gradient(#6aa7d8,#d7a77f)"></div><p>Sed ut perspiciatis unde omnis iste<br>natus error sit voluptatem ....</p></div>
    <div class="news-item" style="top:88px"><div class="thumb" role="img" aria-label="News thumbnail" style="background:linear-gradient(#7fb6e0,#e6c39a)"></div><p>Sed ut perspiciatis unde omnis iste<br>natus error sit voluptatem ....</p></div>
    <div class="news-item last" style="top:136px"><div class="thumb" role="img" aria-label="News thumbnail" style="background:linear-gradient(#b48a70,#e5cbb6)"></div><p>Sed ut perspiciatis unde omnis iste<br>natus error sit voluptatem ....</p></div>
  </section>

  <section class="abs widget" style="top:384px;height:180px">
    <div class="widget-head">Feature interviews</div>
    <div class="interview" style="top:31px">Aliquam molestie mi et imperdiet</div>
    <div class="interview" style="top:55px">Euismod dui purus auctor tellus</div>
    <div class="interview" style="top:79px">Et interdum lacus lectus</div>
    <div class="interview" style="top:104px">Aliquam molestie mi et imperdiet</div>
    <div class="interview" style="top:128px">Euismod dui purus auctor tellus</div>
    <div class="submit">SUBMIT</div>
  </section>
</aside>

<a class="abs social-btn fb"><span>LIKE US ON FRIENDHUB</span><span class="count"><i></i><b>3k</b></span></a>
<a class="abs social-btn tw"><span class="mark"></span><span>JOIN US</span></a>
<a class="abs social-btn pn"><span class="mark"></span><span>PIN WITH US</span></a>

<footer class="abs footer">
  <div class="abs footer-icons">
    <span style="background:#3b5998"></span>
    <span style="background:#1da1e2"></span>
    <span style="background:#f39422"></span>
    <span style="background:#d23e2b"></span>
    <span style="background:#b31217"></span>
    <span style="background:#a7a7a7"></span>
    <span style="background:#f2502c"></span>
  </div>
  <div class="abs copyright">Copyright 2015 – <b>Star Circuit //</b>&nbsp; All Right Reserved</div>
</footer>
</body>
</html>
```